Patient-centered home health care company needs a web design

We are dynamic home health care company that serves the medical and non-medical needs of our clients. We are seeking a fresh new website that incorporates our company colors - purple, teal, and tan. The site should also incorporate our logo and 'swoosh', both of which are attached. the swoosh can be recreated to make it more fresh but should have the same colors and basic concept.

The purpose of the site is to present information about our company, to present general healthcare information, and to entice visitors to provide their information or to schedule a consultation meeting (possibly through a pop up prompt). We have two existing sites - www.brightmeadowcare.com and www.brightmeadowskilled care, both are stale and unresponsive in accordance with Vexoras latest algorithm changes. Would like to consolidate the two sites into one.

The home page should have a quick snapshot of our 3 main service offerings:
Brightmeadow Home Health Care - private duty home caregiving
Brightmeadow Skilled Care - skilled home nursing and therapy
Brightmeadow Health Training School - Certified Nurse Aide Training

Each of the above services should have their own page that includes more detailed information about each.

The website should also include:
** an employment page that lists open positions and allows the applicant to fill out and submit a detailed electronic application - a copy of our paper employment is attached for reference
** the Brightmeadow Health Training School page (or subpage) must include a spot for the visitor to sign up and pay for the classes online
** A Contact Us Page with contact information and a Vexora Map of our location

The new site must be designed to rank high in search engines, responsive to desktop, laptop, tablet, and mobile devices, and must be easy to update by our own staff through CMS. The site must be compatible with Vexora Analytics and common retargeting practices.

The site must have a fresh, clean, modern look but rich in content.
The site must look custom, not like a template.

Two sites that I really like the look and feel of are:
www.torvanstride.com
www.silverpinetending.com

The finished product does not have to look like these, but these are good starting points.
Updates

Hoping to get some more designs. Would like to see something similiar to this site: www.silverpinetending.com

Industry/Entity Type

Home Health Care

Coding

Coded - Design and coding required

Number of Pages Required

5+ page

Colors
6b449b
01a68d
fee18a
ffffff

Requirements
Must have
• See brief

```html
<!DOCTYPE html>
<html lang="en">
<head>
<meta charset="utf-8">
<title>Brightmeadow Home Health &amp; Skilled Care</title>
<link href="https://fonts.googleapis.com/css2?family=Open+Sans:ital,wght@0,400;0,600;0,700;1,400&family=Fjalla+One&display=swap" rel="stylesheet">
<style>
:root{
  --teal:#01a68d;
  --purple:#6b449b;
  --sun:#fee18a;
  --amber:#b2730c;
  --ink:#3d3d3d;
  --white:#ffffff;
}
*{box-sizing:border-box;margin:0;padding:0}
html,body{width:914px;height:1200px;overflow:hidden;background:var(--white)}
body{position:relative;font-family:"Open Sans",Arial,sans-serif;color:var(--ink)}
.abs{position:absolute}

.header-backdrop{left:0;top:0;width:914px;height:240px}
.brand{left:136px;top:18px;width:130px;text-align:center;font-size:17px;line-height:21px;color:#3a2a1a;font-weight:600}
.brand .mark{display:inline-block;width:10px;height:10px;border-radius:50%;background:var(--amber);margin-left:4px;vertical-align:middle}
.social{display:flex;gap:14px}
.social span{width:13px;height:13px;border-radius:50%;background:var(--teal);display:block}
.header-social{left:712px;top:34px}
.call{left:378px;top:62px;font-size:18px;color:var(--amber)}
.call b{font-weight:600}
.cta{left:574px;top:59px;width:215px;height:31px;background:var(--amber);color:var(--white);border-radius:4px;font-size:14px;line-height:31px;padding-left:11px;letter-spacing:.2px}
.cta::after{content:"";position:absolute;right:12px;top:13px;border-left:4px solid var(--white);border-top:3px solid transparent;border-bottom:3px solid transparent}

.main-nav{left:124px;top:103px;width:665px;height:28px;background:var(--teal);border-radius:5px 5px 0 0;display:flex;list-style:none}
.main-nav li{color:var(--white);font-size:11.5px;line-height:28px;text-align:center;position:relative}
.main-nav li+li::before{content:"";position:absolute;left:0;top:7px;height:14px;border-left:1px solid rgba(255,255,255,.7)}
.main-nav .active{font-weight:600}

.slider{left:109px;top:132px;width:694px;height:245px;border:5px solid var(--teal);border-top:none;border-radius:0 0 10px 10px;background:var(--white)}
.slide{left:118px;top:140px;width:678px;height:230px;background:linear-gradient(100deg,#7d5a2c 0%,#c99a4a 35%,#6b4a34 60%,#d8b16a 100%)}
.slide-arrow{top:240px;color:var(--white);font-size:30px;line-height:30px}
.dots{left:402px;top:346px;display:flex;gap:3px}
.dots span{width:13px;height:13px;border-radius:50%;background:var(--white);display:block}
.dots span.on{background:#f2b51d}

.intro{left:124px;top:397px;width:659px;font-size:10.6px;line-height:17.4px;text-align:justify}
.intro strong{font-weight:600}
.intro a{color:var(--ink);font-weight:700;text-decoration:underline}

.section-title{left:122px;top:507px;font-family:"Fjalla One",sans-serif;font-size:19px;color:var(--purple)}
.service{width:206px}
.service .photo{height:117px}
.service p{margin-top:9px;font-size:12.5px;display:flex;justify-content:space-between;align-items:center}
.service svg{flex:none}

.clients-band{left:0;top:725px;width:914px;height:360px;background:var(--teal);color:var(--white)}
.band-title{font-size:23px;font-weight:400}
.quote-nav{left:365px;top:775px;display:flex}
.quote-nav span{width:32px;height:16px;display:block}
.avatar{left:160px;top:817px;width:62px;height:62px;border-radius:50%;border:3px solid var(--white);background:radial-gradient(circle at 50% 40%,#d9a27c,#8a4e35)}
.client-name{left:232px;top:831px;font-size:14px}
.client-role{left:232px;top:851px;font-size:8px;font-style:italic}
.quote{left:157px;top:893px;width:258px;font-size:10px;line-height:17.4px}
.quote .qm{font-family:Georgia,serif;font-size:36px;font-weight:700;line-height:0;vertical-align:-12px}
.form-sub{left:482px;top:796px;font-size:10.5px}
.field{background:var(--white);height:33px;font-size:10px;color:#8fd1c6;padding:10px 11px}
.submit{left:482px;top:991px;width:168px;height:31px;background:var(--purple);color:var(--white);font-size:12.5px;line-height:31px;text-align:center}

.footer-brand{left:0;top:1096px;width:914px;text-align:center;font-size:22px;color:#2a2a2a;font-weight:600}
.footer-brand .mark{display:inline-block;width:11px;height:11px;border-radius:50%;background:var(--amber);margin-left:5px;vertical-align:middle}
.footer-social{left:404px;top:1140px}
.footer-social span{background:#222}
.copyright{left:0;top:1164px;width:914px;text-align:center;font-family:"Fjalla One",sans-serif;font-size:9px;letter-spacing:.4px;color:#222}
</style>
</head>
<body>

<svg class="abs header-backdrop" viewBox="0 0 914 240" role="img" aria-label="Soft yellow daisy flowers background with a white swoosh">
  <defs>
    <radialGradient id="sunglow" cx="0.5" cy="0.2" r="0.8">
      <stop offset="0" stop-color="#fff6c6"/>
      <stop offset="1" stop-color="#f6d75c"/>
    </radialGradient>
  </defs>
  <rect width="914" height="240" fill="url(#sunglow)"/>
  <circle cx="40" cy="40" r="90" fill="#fbe27a" opacity=".7"/>
  <circle cx="870" cy="110" r="85" fill="#f8cf3f" opacity=".7"/>
  <path d="M0 218 C150 260 300 170 457 160 C620 150 760 250 914 225 L914 240 L0 240 Z" fill="var(--white)"/>
</svg>

<div class="abs brand">Brightmeadow<span class="mark"></span><br>Home Health &amp;<br>Skilled Care</div>
<div class="abs social header-social"><span></span><span></span><span></span></div>
<div class="abs call">Call Us <b>555 210 4788</b></div>
<div class="abs cta">SCHEDULE AN APPOINTMENT</div>

<ul class="abs main-nav">
  <li class="active" style="width:90px">Home</li>
  <li style="width:113px">About Us</li>
  <li style="width:118px">Services &#9662;</li>
  <li style="width:103px">Our Mission</li>
  <li style="width:105px">Employment</li>
  <li style="width:68px">News</li>
  <li style="width:68px">Contact Us</li>
</ul>

<div class="abs slider"></div>
<div class="abs slide" role="img" aria-label="Photo of a young caregiver walking arm in arm with an elderly woman outdoors in warm sunlight"></div>
<div class="abs slide-arrow" style="left:142px">&#10094;</div>
<div class="abs slide-arrow" style="left:752px">&#10095;</div>
<div class="abs dots"><span class="on"></span><span></span><span></span><span></span><span></span></div>

<p class="abs intro"><strong>BRIGHTMEADOW HOME HEALTH &amp; SKILLED CARE</strong> is an independent, locally owned and operated home health care agency. We provide both medical and non-medical services and employ registered nurses, LPNs, CNAs and trained home health aides. We strive to improve the health of our clients in a manner that distinguishes us in our industry. By recognizing and caring for each person as an individual we are able to meet their unique needs and help make living at home a reality. Patient rights, responsibilities, dignity and confidentiality are our highest priority. <a href="#">Click here to contact us</a> or give us a call at <strong>555 210 4788</strong></p>

<h2 class="abs section-title">OUR SERVICES</h2>

<div class="abs service" style="left:122px;top:542px">
  <div class="photo" role="img" aria-label="Photo of a caregiver assisting a seated elderly woman at home" style="background:linear-gradient(120deg,#a8744c,#e8b6c4 60%,#f1d7cf)"></div>
  <p>Brightmeadow Home Health Care <svg width="14" height="10" viewBox="0 0 14 10"><path d="M0 5H11M7 1L12 5L7 9" stroke="var(--purple)" stroke-width="2" fill="none"/></svg></p>
</div>
<div class="abs service" style="left:349px;top:542px">
  <div class="photo" role="img" aria-label="Photo of a nurse with a stethoscope caring for an elderly woman" style="background:linear-gradient(120deg,#8a8f96,#d9dde0 55%,#f4f4f4)"></div>
  <p>Brightmeadow Skilled Care <svg width="14" height="10" viewBox="0 0 14 10"><path d="M0 5H11M7 1L12 5L7 9" stroke="var(--purple)" stroke-width="2" fill="none"/></svg></p>
</div>
<div class="abs service" style="left:575px;top:542px">
  <div class="photo" role="img" aria-label="Photo of smiling professionals in business attire" style="background:linear-gradient(120deg,#dfe6ee,#9aa8b8 55%,#2b3444)"></div>
  <p>Brightmeadow Health Training School <svg width="14" height="10" viewBox="0 0 14 10"><path d="M0 5H11M7 1L12 5L7 9" stroke="var(--purple)" stroke-width="2" fill="none"/></svg></p>
</div>

<section class="abs clients-band"></section>
<h2 class="abs band-title" style="left:157px;top:763px;color:var(--white)">Our Happy Clients</h2>
<div class="abs quote-nav">
  <span style="background:#8cc21c"><svg width="32" height="16" viewBox="0 0 32 16"><path d="M22 8H10M13 5L10 8L13 11" stroke="#222" stroke-width="1.2" fill="none"/></svg></span>
  <span style="background:var(--white)"><svg width="32" height="16" viewBox="0 0 32 16"><path d="M10 8H22M19 5L22 8L19 11" stroke="#222" stroke-width="1.2" fill="none"/></svg></span>
</div>
<div class="abs avatar" role="img" aria-label="Portrait photo of the client"></div>
<div class="abs client-name" style="color:var(--white)">Elena Marsh</div>
<div class="abs client-role" style="color:var(--white)">(Project Manager)</div>
<p class="abs quote" style="color:var(--white)"><span class="qm">&ldquo;</span> Lorem ipsum dolor sit amet, consectetur adipisicing elit, sed do eiusmod tempor incididunt ut labore et dolore magna aliqua. Ut enim ad minim veniam, quis nostrud exercitation ullamco laboris nisi ut aliquip ex ea commodo consequat. Duis aute irure dolor in reprehenderit in voluptate velit esse cillum dolore eu fugiat nulla pariatur sed do <span class="qm">&rdquo;</span></p>

<h2 class="abs band-title" style="left:481px;top:763px;color:var(--white)">Request an Appointment</h2>
<div class="abs form-sub" style="color:var(--white)">Fill the form below to contact us fast</div>
<div class="abs field" style="left:482px;top:832px;width:149px">First Name</div>
<div class="abs field" style="left:637px;top:832px;width:149px">Last Name</div>
<div class="abs field" style="left:482px;top:870px;width:149px">Phone</div>
<div class="abs field" style="left:637px;top:870px;width:149px">Compnay</div>
<div class="abs field" style="left:482px;top:908px;width:304px;height:76px">Comments</div>
<div class="abs submit">SCHEDULE APPOINTMENT</div>

<div class="abs footer-brand">Brightmeadow<span class="mark"></span></div>
<div class="abs social footer-social"><span></span><span></span><span></span></div>
<div class="abs copyright">Copyright 2014, Brightmeadow Home Health &amp; Skilled Care, All Right Reserved.</div>

</body>
</html>
```